New Equipment Rental Location Postcard *

We have a new equipment rental location that we opened and want to do a bulk mailing with a postcard to advertise. The post card has to be 6.5" x 9" and printed on both sides. The back side has to have the postage icons on them like in the example postcard I have uploaded. Also I have included our logo in the attachments. The attachement "capture' is just an example of how the back should look with the 2 postage icons. I have also uploaded those 2 graphics.

Rental

• I would like to convey "New Location". Also would like our customers to know that our rental fleet consists of "Well Maintained and New Equipment". Also would like to say that we will beat any competitors price. Also on the back, I want to include a 10% discount coupon (almost like the postcard I included as an example.
• Lastly if you could list the following industries that we provide rentals for:
• Landscape / Tree Professionals
• Contractors
• Do-It-yourself'ers
• Home and Office Supplies
• If we could find somewhere to list that we ALSO have 60' bucket/chipper trucks, as well as 12", 14", & 18" chippers for rent at an affordable price that would be great.
• As some of the backdrops we could incorporate Bex Skid Steers, Darno Power tools, as well as Brantworthian bucket trucks and Quillon chippers. I have attached some pictures as examples. We don't have to use these, just some ideas. I would like to show some pictures to show the equipment we rent (like the attached ones)

```html
<!DOCTYPE html>
<html lang="en">
<head>
<meta charset="utf-8">
<title>Kestrel Rentals – New Location Postcard</title>
<link rel="stylesheet" href="https://fonts.googleapis.com/css2?family=Fredoka:wght@600;700&family=Lato:wght@700;900&family=Arimo:wght@400;700&display=swap">
<style>
  :root {
    --stage: #3a3a3c;
    --navy: #0f4069;
    --navy-deep: #0b3a60;
    --orange: #fdc36e;
    --grey: #c4c6c9;
    --sky: #d6e6f4;
    --white: #ffffff;
    --ink: #1a1a1a;
  }
  * { margin: 0; padding: 0; box-sizing: border-box; }
  html, body { width: 928px; height: 1200px; overflow: hidden; }
  body { background: var(--stage); position: relative; font-family: "Fredoka", sans-serif; }

  .card {
    position: absolute; left: 118px; width: 692px; height: 501px;
    overflow: hidden; background: var(--white);
    box-shadow: 0 2px 6px rgba(0,0,0,.35);
  }
  .card--front { top: 93px; background: linear-gradient(180deg, var(--sky) 0%, var(--white) 22%); }
  .card--back { top: 606px; background: linear-gradient(180deg, var(--sky) 0%, var(--white) 20%); }

  .front-shapes { position: absolute; inset: 0; }

  .headline { position: absolute; color: var(--navy); font-weight: 700; line-height: 1; letter-spacing: -2px; }
  .headline--new { left: 52px; top: 22px; font-size: 100px; letter-spacing: -1px; }
  .headline--location { left: 28px; top: 94px; font-size: 92px; letter-spacing: -4px; }

  .brand {
    position: absolute; left: 420px; top: 92px; width: 240px;
    color: var(--navy); font-family: "Fredoka", sans-serif; font-weight: 700;
    text-align: center; line-height: 1;
  }
  .brand__name { font-size: 40px; letter-spacing: 2px; display: block; }
  .brand__sub { font-size: 15px; letter-spacing: 7px; display: block; margin-top: 6px; }

  .tagline {
    position: absolute; left: 30px; top: 194px; color: var(--orange);
    font-size: 36px; font-weight: 700; line-height: 1.1; letter-spacing: -0.5px;
  }

  .fleet-note {
    position: absolute; left: 30px; top: 353px; width: 250px;
    color: var(--navy); font-size: 19px; font-weight: 700; line-height: 1.22; letter-spacing: -0.3px;
  }

  .equipment-photo {
    position: absolute; left: 262px; top: 172px; width: 428px; height: 324px;
    border-radius: 40% 20% 10% 30% / 30% 30% 10% 20%;
    background: radial-gradient(ellipse at 60% 50%, #f2c744 0%, #e7b83a 45%, rgba(231,184,58,.0) 75%);
  }

  .back-panel { position: absolute; inset: 0; }

  .price-promise {
    position: absolute; left: 41px; top: 76px; color: var(--white);
    font-size: 30px; font-weight: 700; line-height: 1.12; letter-spacing: -0.3px;
  }

  .coupon {
    position: absolute; left: 38px; top: 178px; width: 304px; height: 126px;
    background: var(--white); border: 3px dashed var(--orange);
    display: flex; align-items: center; justify-content: center;
  }
  .coupon__value { font-family: "Lato", sans-serif; font-weight: 900; font-size: 57px; color: var(--navy); letter-spacing: -1px; }

  .industries {
    position: absolute; left: 40px; top: 344px; list-style: none;
    color: var(--white); font-size: 18px; font-weight: 700; line-height: 24px; letter-spacing: -0.2px;
  }
  .industries li::before { content: "\25CF"; font-size: 14px; margin-right: 5px; vertical-align: 1px; }

  .postage-indicia {
    position: absolute; left: 597px; top: 40px; width: 58px; height: 56px;
    border: 1px solid #555; font-family: "Arimo", sans-serif; font-size: 7.4px;
    color: var(--ink); text-align: center; line-height: 9.2px; padding-top: 3px;
  }
  .postage-indicia b { font-weight: 700; }

  .address-block {
    position: absolute; left: 378px; top: 202px; width: 192px; height: 77px;
    border: 1px solid #666; font-family: "Arimo", sans-serif; color: var(--ink);
  }
  .address-block__route { position: absolute; left: 58px; top: 10px; font-size: 9px; }
  .address-block__recipient { position: absolute; left: 14px; top: 36px; font-size: 11.5px; line-height: 13px; }

  .address-line { position: absolute; left: 379px; width: 276px; height: 1px; background: #444; }
</style>
</head>
<body>

<section class="card card--front">
  <svg class="front-shapes" width="692" height="501" viewBox="0 0 692 501" aria-hidden="true">
    <path d="M0 185 H520 Q560 188 568 230 L574 283 H0 Z" fill="var(--navy)"/>
    <path d="M0 315 C120 300 200 330 280 298 C400 262 560 300 692 272 L692 290 C560 312 400 282 282 314 C200 340 120 312 0 326 Z" fill="var(--grey)"/>
    <path d="M0 326 C120 312 200 340 282 314 C400 282 560 312 692 290 V501 H0 Z" fill="var(--orange)"/>
  </svg>

  <h1 class="headline headline--new">NEW</h1>
  <h1 class="headline headline--location">location</h1>

  <div class="brand">
    <span class="brand__name">KESTREL</span>
    <span class="brand__sub">RENTALS</span>
  </div>

  <h2 class="tagline">Well Maintained &amp;<br>New Equipment</h2>

  <p class="fleet-note">We ALSO have 60' bucket/chipper trucks, as well as 12", 14", &amp; 18" chippers for rent at an affordable price</p>

  <div class="equipment-photo" role="img" aria-label="Photo of a yellow Bex skid steer loader in front of a yellow Quillon wood chipper"></div>
</section>

<section class="card card--back">
  <svg class="back-panel" width="692" height="502" viewBox="0 0 692 502" aria-hidden="true">
    <path d="M0 0 H380 L346 502 H0 Z" fill="var(--orange)"/>
    <path d="M0 0 H372 L338 502 H0 Z" fill="var(--navy-deep)"/>
  </svg>

  <h2 class="price-promise">We Will Beat Any<br>Competitors Price</h2>

  <div class="coupon"><span class="coupon__value">10% OFF</span></div>

  <ul class="industries">
    <li>Landscape / Tree Professionals</li>
    <li>Contractors</li>
    <li>Do-It-yourself'ers</li>
    <li>Home and Office Supplies</li>
  </ul>

  <div class="postage-indicia">PRSRT STD<br>ECRWSS<br>U.S. Postage<br><b>PAID</b><br>EDDM RETAIL</div>

  <div class="address-block">
    <span class="address-block__route">****************ECRWSS****</span>
    <span class="address-block__recipient">Local<br>Postal Customer</span>
  </div>

  <div class="address-line" style="top:357px"></div>
  <div class="address-line" style="top:396px"></div>
  <div class="address-line" style="top:434px"></div>
</section>

</body>
</html>
```